VFX Company Business Card Design Project

The Pixel Harbor is a decentralized Visual Effects Studio servicing the television and feature film industries.
Project Brief:
Take our logo that was previously designed on Sketch Forum and make a double sided business card.
Requirements:
- Card MUST be double sided.
- Front of card MUST have the yellow part of our logo against the dark grey background.
- Back of card is completely up to the designer.
- Back of card must include the complete company logo.
Please follow these File Preparation guidelines:
http://printmarlow.example/infopage?file=filetype_en&s=PrintMarlow_new&lang=en
Industry/Entity Type
Business
Look and feel
Each slider illustrates characteristics of the customer's brand and the style your logo design should communicate.

```html
<!DOCTYPE html>
<html lang="en">
<head>
<meta charset="utf-8">
<title>The Pixel Harbor – Business Card</title>
<link rel="stylesheet" href="https://fonts.googleapis.com/css2?family=Open+Sans:wght@400;600;700&display=swap">
<style>
  :root {
    --page: #e9e7e3;
    --card-dark: #2c2c2e;
    --brand-yellow: #f2bd1f;
    --band-grey: #a3a4a6;
    --band-grey-light: #c9caca;
    --text-light: #ffffff;
    --text-muted: #d8d8d8;
  }
  * { margin: 0; padding: 0; box-sizing: border-box; }
  html, body {
    width: 1200px; height: 900px; overflow: hidden;
    background: var(--page);
    font-family: "Open Sans", Arial, sans-serif;
  }
  .sheet {
    width: 1200px; height: 900px;
    display: flex; flex-direction: column;
    align-items: center; justify-content: center; gap: 36px;
  }
  .card {
    position: relative;
    width: 700px; height: 400px;
    background: var(--card-dark);
    border-radius: 4px;
    box-shadow: 0 6px 18px rgba(0,0,0,0.18);
    overflow: hidden;
  }
  /* Front: brand name in yellow on dark grey */
  .card--front { display: flex; align-items: center; justify-content: center; gap: 22px; }
  .brand-dot {
    width: 46px; height: 46px; border-radius: 50%;
    background: var(--brand-yellow);
  }
  .brand-name {
    color: var(--brand-yellow);
    font-weight: 700; font-size: 52px; letter-spacing: 1px;
  }
  /* Back: contact side */
  .card-waves { position: absolute; inset: 0; width: 100%; height: 100%; }
  .back-brand {
    position: absolute; top: 34px; left: 40px;
    display: flex; align-items: center; gap: 12px;
  }
  .back-brand .brand-dot { width: 24px; height: 24px; }
  .back-brand .brand-name { font-size: 28px; }
  .contact {
    position: absolute; top: 118px; right: 40px;
    text-align: right; color: var(--text-light);
  }
  .contact-name { font-weight: 700; font-size: 28px; line-height: 1.1; }
  .contact-role { font-size: 14px; color: var(--text-muted); margin-bottom: 14px; }
  .contact-lines { list-style: none; font-size: 14px; line-height: 1.55; font-weight: 600; }
  .contact-lines li { display: flex; justify-content: flex-end; align-items: center; gap: 8px; }
  .contact-icon { width: 13px; height: 13px; flex: none; }
  .contact-icon--blank { visibility: hidden; }
</style>
</head>
<body>
<main class="sheet">
  <section class="card card--front" aria-label="Card front">
    <span class="brand-dot"></span>
    <span class="brand-name">The Pixel Harbor</span>
  </section>

  <section class="card card--back" aria-label="Card back">
    <svg class="card-waves" viewBox="0 0 700 400" preserveAspectRatio="none" aria-hidden="true">
      <path d="M0,170 C180,160 330,250 470,300 C560,332 630,345 700,350 L700,400 L0,400 Z" fill="var(--band-grey-light)"/>
      <path d="M0,182 C190,172 340,262 480,312 C570,342 635,355 700,360 L700,400 L0,400 Z" fill="var(--band-grey)"/>
      <path d="M0,200 C200,195 340,285 480,335 C560,362 630,372 700,376 L700,400 L0,400 Z" fill="var(--brand-yellow)"/>
    </svg>

    <div class="back-brand">
      <span class="brand-dot"></span>
      <span class="brand-name">The Pixel Harbor</span>
    </div>

    <div class="contact">
      <p class="contact-name">Daniel Hart</p>
      <p class="contact-role">President</p>
      <ul class="contact-lines">
        <li>P.O Box 4100, Harbour Hall AU 3KE
          <svg class="contact-icon" viewBox="0 0 12 12"><path d="M6 0.5a4 4 0 0 0-4 4c0 3 4 7 4 7s4-4 4-7a4 4 0 0 0-4-4z" fill="var(--brand-yellow)"/><circle cx="6" cy="4.5" r="1.4" fill="var(--card-dark)"/></svg>
        </li>
        <li>+01 555 01234
          <svg class="contact-icon" viewBox="0 0 12 12"><path d="M2.5 0.8l2 2.2-1 1.4c.7 1.6 1.8 2.7 3.4 3.4l1.4-1 2.2 2-1.2 1.9C4.8 10.4 1.3 6.9.6 2z" fill="var(--brand-yellow)"/></svg>
        </li>
        <li>info@pixelharbor.example
          <svg class="contact-icon" viewBox="0 0 12 12"><rect x="0.5" y="2" width="11" height="8" rx="1" fill="var(--brand-yellow)"/><path d="M1 2.6l5 3.8 5-3.8" fill="none" stroke="var(--card-dark)" stroke-width="1"/></svg>
        </li>
        <li>www.pixelharbor.example
          <svg class="contact-icon" viewBox="0 0 12 12"><circle cx="6" cy="6" r="5" fill="none" stroke="var(--brand-yellow)" stroke-width="1.4"/><path d="M1 6h10M6 1c2 2.5 2 7.5 0 10M6 1c-2 2.5-2 7.5 0 10" fill="none" stroke="var(--brand-yellow)" stroke-width="1"/></svg>
        </li>
      </ul>
    </div>
  </section>
</main>
</body>
</html>
```